Skin Care Package Design

Hello,

I have a unique situation at hand. I already posted a project for this and we chose a winner but we ended up having trademark concerns so we need to modify the designs on the package.

We do not blame the designer in any way and we think that they did an incredible job. We have also chosen him as the winner and paid him so we have full right to share this and have 100% ownership of the design.

Our biggest competitor is Lumo Brisk Dot. We need to be careful not to have a design that is too close to theirs. I think the color red is fine in general, but we need to stay away from any shapes/designs that would be considered similar. They have a partial circle design on the corner and ours is to similar in our opinion - our mistake.

Our name is no longer Velden Face Co. It is now TOLVEN or Tolven.

We need:
1. Velden Face Co removed and "TOLVEN" or "Tolven" put in it's place. You do NOT have to leave the rectangle border. We do not have a design file or the logo yet. We like modern fonts.
2. Please remove the circular designs in the corners. It too closely resembles our competitors package. A square or some other unique concept would work. Feel free to use your imagination. We loved our current design because it's clean and simple but looks good.
3. Please don't mess with the text. We like it and the layout. Our focus is on the color/s and unique design that is going to replace the circle in the corners.
4. Please change "144" in the bottom right to "36".
5. The color red is still fine but we would be curious to see other colors like the green or blue that Dunmel has or maybe a taupe. Use your imagination. We really want colors that pop and grab your attention. Feel free to use more than one color.

I have uploaded two images.
1. Lumo - Is our competitor's package.
2. Velden Face Co is our previous/current package design.

Package deminsions: 5”x3.4”x0.47”

Thanks! Good luck!

Target Market(s)

Male & female. We don't want the package design to be too masculine or too feminine.

Industry/Entity Type

Skin care, health & cosmetics.

Font styles to use
Sans Serif

Requirements
Must have
• You can search acne patch brands on Shopnest and see our competitors. We want ours to look better than Lumo Brisk Dot. They are the top seller. They have a simple and clean design but the red really grabs your eye. There are a ton of brands on the Shopnest page so it's important that the package looks good and the color/s catch your eye.

```html
<!DOCTYPE html>
<html lang="en">
<head>
<meta charset="utf-8">
<title>Tolven – The Acne Patch</title>
<link rel="stylesheet" href="https://fonts.googleapis.com/css2?family=Poppins:wght@300;400;500;600;700&display=swap">
<style>
  :root {
    --stage: #e3e5e8;
    --card: #ffffff;
    --brand-red: #ef3e42;
    --ink: #3b3b3b;
    --ink-soft: #454545;
    --white: #ffffff;
    --patch-tone: #ecebec;
  }
  * { box-sizing: border-box; margin: 0; padding: 0; }
  html, body {
    width: 1200px;
    height: 867px;
    overflow: hidden;
    background: var(--stage);
    font-family: "Poppins", sans-serif;
  }
  .pack-front {
    position: absolute;
    left: 344px;
    top: 43px;
    width: 511px;
    height: 780px;
    background: var(--card);
    box-shadow: 0 6px 24px rgba(0,0,0,0.10);
    overflow: hidden;
  }
  .brand-name {
    position: absolute;
    left: 52px;
    top: 140px;
    font-size: 43px;
    font-weight: 500;
    letter-spacing: 7px;
    color: var(--ink);
    line-height: 1;
  }
  .title-panel {
    position: absolute;
    left: 0;
    top: 207px;
    width: 337px;
    height: 360px;
    background: var(--brand-red);
    border-radius: 0 10px 10px 0;
  }
  .product-title {
    position: absolute;
    left: 55px;
    top: 38px;
    color: var(--white);
    font-size: 56px;
    line-height: 55px;
    letter-spacing: 3px;
  }
  .product-title span { display: block; }
  .product-title .light { font-weight: 300; }
  .product-title .bold { font-weight: 700; }
  .title-rule {
    position: absolute;
    left: 55px;
    top: 225px;
    width: 148px;
    height: 1px;
    background: var(--white);
  }
  .tagline {
    position: absolute;
    left: 55px;
    top: 254px;
    color: var(--white);
    font-size: 26.5px;
    font-weight: 500;
    line-height: 28px;
  }
  .patch-visual {
    position: absolute;
    left: 322px;
    top: 337px;
    width: 128px;
    height: 128px;
    border-radius: 50%;
    background: var(--patch-tone);
  }
  .patch-label {
    position: absolute;
    left: 416px;
    top: 328px;
    font-size: 11px;
    line-height: 1;
    color: var(--ink);
    transform: rotate(50deg);
    transform-origin: left top;
    white-space: nowrap;
  }
  .slogan {
    position: absolute;
    left: 55px;
    top: 597px;
    font-size: 20px;
    font-weight: 500;
    color: var(--ink-soft);
    line-height: 1;
  }
  .slogan-rule {
    position: absolute;
    left: 55px;
    top: 625px;
    width: 132px;
    height: 2px;
    background: var(--brand-red);
  }
  .description {
    position: absolute;
    left: 55px;
    top: 633px;
    width: 260px;
    font-size: 13.5px;
    line-height: 22.4px;
    color: var(--ink-soft);
  }
  .count-badge {
    position: absolute;
    left: 336px;
    top: 580px;
    width: 140px;
    height: 140px;
  }
</style>
</head>
<body>
  <main class="pack-front">
    <div class="brand-name">TOLVEN.</div>

    <section class="title-panel">
      <h1 class="product-title">
        <span class="light">THE</span>
        <span class="bold">ACNE</span>
        <span class="light">PATCH</span>
      </h1>
      <div class="title-rule"></div>
      <p class="tagline">Ideal for<br>surface spots.</p>
    </section>

    <div class="patch-visual" role="img" aria-label="Illustration of a clear round hydrocolloid patch with a peeling edge"></div>
    <div class="patch-label">Transparent</div>

    <p class="slogan">Your blemish wizard.</p>
    <div class="slogan-rule"></div>
    <p class="description">Gently absorbs gunk in 6 - 8 hours<br>&amp; approves the look of pimples<br>overnight.</p>

    <svg class="count-badge" viewBox="0 0 140 140" aria-label="36 hydrocolloid patches, 8mm and 12mm sizes, non-drying">
      <defs>
        <path id="badge-top-arc" d="M70,110 A40,40 0 1 1 70,30 A40,40 0 1 1 70,110"/>
        <path id="badge-bottom-arc" d="M20,70 A50,50 0 0 0 120,70"/>
      </defs>
      <g font-family="Poppins, sans-serif" fill="#3b3b3b">
        <text font-size="13.5" font-weight="500" letter-spacing="0.6">
          <textPath href="#badge-top-arc" startOffset="50%" text-anchor="middle">8MM &amp; 12 MM SIZES</textPath>
        </text>
        <text font-size="13.5" font-weight="500" letter-spacing="1">
          <textPath href="#badge-bottom-arc" startOffset="50%" text-anchor="middle">NON - DRYING</textPath>
        </text>
        <text x="70" y="72" font-size="40" font-weight="700" text-anchor="middle" letter-spacing="-1">36</text>
        <text x="70" y="84" font-size="8.5" font-weight="500" text-anchor="middle">HYDROCOLLOID</text>
        <text x="70" y="95" font-size="8.5" font-weight="500" text-anchor="middle">PATCHES</text>
        <text x="24" y="83" font-size="9" text-anchor="middle">★</text>
        <text x="116" y="83" font-size="9" text-anchor="middle">★</text>
      </g>
    </svg>
  </main>
</body>
</html>
```